Design of Premium Instant Tea Packaging (Tea in 3 seconds)

We need a fully packaging and sachets design for our new premium instant tea (Tea in 3 seconds) collection to our new brand BrimLeaf. The company is based in Norway and are founded by two Norwegian with a passion for tea and with a mission to share our passion in a faster and easier manner.

We would like a design that gives an exclusive, healthy, tasty and warm feeling. The design should communicate instant tea of high quality.

The tea is one of the first premium instant tea on the market and should give the customer a feeling of exclusive innovation, A new tea company is in town. We don't want to be similar to other old granny tea companies and we hate tea bags :P.

About our products. We offer two different Flavours:
Brim Hibiscus and Brim Lemon. The Brim Hibiscus is sweet and red as blood in its color.

We are looking for a universal design where we can change the color and text based on the flavors. So is important that we get the edible design for front and back of the packages and sachets. Each package contains 10 small sachets where the design of the sachets should be a similar design as the packages itself.

I will provide an example picture/template (just a guideline, not obligatory) from the factory and the sachets, but also from our competitors. Is important that both packaging design and sachets design is editable from both sides if we in the future add new flavors or text.

I will also provide a word file with the necessary text on the pack of the packaging and Nutrition Facts for both of the two flavors. Important that the ingredients are a least in both Norwegian (N) and English (GB). The word file also contains the company information, put on the back of the packaging.

Attached pls find two pictures of design template. Maybe you need them when designing. It's the dimension of 10 sachets/box and 0.6g/sachet the factory use. Our logo BrimLeaf should be on the packaging and the sachets. I also provided the logo in editable format.

Brim Instant Lemon:
GB Ingredients : Lemon, black tea
N Ingredienser: Sitron, svart te

Brim Instant Hibiscus:
GB Ingredients: Hibiscus, rose, black tea and stevia extract
N Ingredienser: Hibiscus, rose, svart te og stevia ekstrakt

Experience the new generation of tea! BrimLeaf® is one of the world fist premium instant tea. Made from real fruit and whole tea leaf, you get incredible tea in seconds. Based on patented cold-brewed technology provide you with the essence of tea, without the need for sugar or preservatives. Brim with health, Brim with taste!

Distributed by Korvenet AS®
PO BOX: 4027
Oslo, Mørkedalsgata 5, Norway
Learn more at BrimLeaf.example

Hope your design can help us stand out from the crowd.

With best regards,

Torvald
CEO of Korvenet As

Target Market(s)

The beverages market, or more correctly the tea market.
The product is Premium Instant Tea.

Font styles to use
Serif

Colors

Designer to choose colors to be used in the design.

Requirements
Must have
• The name of the tea flavor in its representative color.
• Brim Instant Lemon
• Premium Black tea (Smaller letters)
• Brim Instant Hibiscus
• Premium Herbal Tea (Smaller letters)
• General facts:
• * 100 % Natural, no additives, artificial flavors or preventative.
• * 0 fat/ 0 Sugar / 0 Calories.
• * In Crystal instead of tea powder or tea bag.
• * It is soluble in 3 seconds with 200 ml to 300 ml hot or cold pure water.
• Looking for a design where we can change the color and text based on the different flavors. So is important that we get the edible design for the and back of the packages and sachets.
• Ingredients in Norwegian (N) and English(GB) and nutrition values in Norwegian and if possible in English. Remember the company information (provided in the packeging.docx) at the back with a link to our website, www.BrimLeaf.example.
• Must show how the product works on the front and the back. Remember instant tea in 3 seconds from sachets. 10 sachets in each pack, should be a part of the front information, see provided examples.
• Important that we can easily change it our self with affinity or other programs, based on new text or flavor. So we need 360-degree design, so we can change the back and the front, based on what our factory can print out.
• Remember that the design should be reused many times, not just for one of those two flavors above. Simple, but yet elegant and upmarket.
• Each package contains 10 small sachets where the design of the sachets should be a similar design as the packages itself. I will provide an example picture/template from the factory and the sachets, but also from our competitors.
• Is important that both packaging design and sachets design is editable from both sides if we in the future add new flavors or text. I will also provide a word file with the necessary text on the pack of the packaging and Nutrition Facts for both of the two flavors. Important that the ingredients are a least in both Norwegian (N) and English (GB). The word file also contains the company information, put on the back of the packaging.
• Brim Lemon:
• GB Ingredients: Lemon, black tea
• N Ingredienser: Sitron, svart te
• Brim Hibiscus:
• GB Ingredients: Hibiscus, rose, black tea and stevia extract
• N Ingredienser: Hibiscus, rose, svart te og stevia ekstrakt
• Text on the back:
• Experience the new generation of tea! BrimLeaf® is one of the world fist premium instant tea. Made from real fruit and whole tea leaf, you get incredible tea in seconds. Based on patented cold-brewed technology provide you with the essence of tea, without the need for sugar or preservatives. Brim with health, Brim with taste!
• Company information:
• Distributed by Korvenet AS®
• PO BOX: 4027
• Oslo, Mørkedalsgata 5, Norway
• Learn more at www.BrimLeaf.example
Nice to have
• Take a look at Bemo Tea, Vardy Tea and Hollet.
• Especially Hollet since they have a clean and high-class design. https://www.holletleaf.example/tea-by-type/indian-breakfast-25-tea-bags?___SID=U.
• Nice with ® on top of the A on BrimLeaf logo.
• Quiro has also nice designs: https://www.quiroleaf.example/us/en/products/hot.html
• Remember the sticking out / eye-catcher". For both of these proposals, I think that if it had some gold elements in the same way that Sundmark coffee has (a little more expensive for flavor) and that the white color of the proposal one is replaced by light black on the sides and either black or gold in the field where the text. In other words, I think that the packaging should be as identical as possible regardless of taste.
• Feedback for Manufacturer: (Just suggestion from her)
• About the packaging, my suggestion is as follows:
• 1) I think color should match "lemon black tea".We'd better choose the color which in coordination with the flavor, for customer's observation conveniently.
• 2) As for the phrase "cold water instant tea", I think it'd better we remark "stir or shake for better dissolving" or similar meanings in the package. Or describing it by pattern as the attachment FYI. Because these two flavors contain black tea which has enzyme. The molecule of enzyme is a little bigger, so it's a little hard to be totally dissolved by cold water without stirring or shaking.
• Pure tea in hot or cold pure water for you anytime, everywhere on the go (On the back
Should not have
• We hate Parvel, Ashcombe's design. Remember simple, modern and elegant. We are the future of tea, don't make your grandma happy with the design!
• Please avoid using teacups in the design!
• Best regards,
• Torvald

```html
<!DOCTYPE html>
<html lang="en">
<head>
<meta charset="utf-8">
<title>BrimLeaf Premium Instant Tea – Packaging</title>
<link rel="stylesheet" href="https://fonts.googleapis.com/css2?family=Cormorant+Garamond:wght@500&family=Josefin+Sans:wght@300;400;600&display=swap">
<style>
  :root{
    --stage:#e6e9ec;
    --divider:#ffffff;
    --paper:#ffffff;
    --hibiscus:#c98866;
    --lemon:#4f8a86;
    --gold:#dcbc76;
    --ink:#5b5b5b;
    --rule-light:rgba(255,255,255,.75);
    --serif:"Cormorant Garamond", Georgia, serif;
    --sans:"Josefin Sans", "Century Gothic", Arial, sans-serif;
  }
  *{box-sizing:border-box;margin:0;padding:0}
  html,body{width:1079px;height:1200px;overflow:hidden;background:var(--stage)}
  .canvas{position:relative;width:1079px;height:1200px;background:var(--stage);font-family:var(--sans);color:var(--ink)}
  .section-divider{position:absolute;left:0;top:668px;width:1079px;height:10px;background:var(--divider)}

  .pack{position:absolute;width:232px;height:348px;background:var(--paper);box-shadow:0 8px 18px rgba(0,0,0,.08);overflow:hidden}
  .pack--hibiscus{--tone:var(--hibiscus)}
  .pack--lemon{--tone:var(--lemon)}

  /* brand lockup */
  .brand{position:absolute;display:flex;flex-direction:column;align-items:center}
  .brand__dot{width:14px;height:14px;border-radius:50%;background:var(--tone);margin-bottom:6px}
  .brand__name{font-family:var(--serif);font-weight:500;font-size:24px;letter-spacing:1px;color:#4a4a4a;line-height:1}

  /* front */
  .front .brand{left:0;right:0;top:40px}
  .front__band{position:absolute;left:0;top:126px;width:232px;height:222px;background:var(--tone)}
  .front__flavor{position:absolute;left:16px;top:18px;font-size:13.5px;font-weight:600;letter-spacing:2.4px;color:var(--gold);white-space:nowrap}
  .front__list{position:absolute;left:0;top:46px;width:130px}
  .front__item{border-top:1px solid var(--rule-light);padding:9px 0 8px 16px;color:#fff;letter-spacing:1.4px;line-height:1.35}
  .front__item--lead{font-size:10px;padding-top:12px}
  .front__item--small{font-size:6.8px}
  .front__item:last-child{border-bottom:1px solid var(--rule-light)}
  .front__count{position:absolute;left:16px;bottom:14px;font-size:6.5px;letter-spacing:1.4px;color:#fff}
  .leaf-art{position:absolute;background:linear-gradient(135deg,rgba(255,255,255,.22),rgba(255,255,255,.05))}
  .front .leaf-art{right:0;top:20px;width:104px;height:188px}

  /* sachets */
  .sachet{position:absolute;width:350px;height:58px;display:flex;box-shadow:0 6px 12px rgba(0,0,0,.1)}
  .sachet--hibiscus{--tone:var(--hibiscus)}
  .sachet--lemon{--tone:var(--lemon)}
  .sachet__cap{width:80px;background:var(--paper);position:relative}
  .sachet__cap .brand{left:0;right:0;top:14px}
  .sachet__cap .brand__dot{width:8px;height:8px;margin-bottom:3px}
  .sachet__cap .brand__name{font-size:14px}
  .sachet__body{flex:1;background:var(--tone);position:relative;overflow:hidden}
  .sachet__sub{position:absolute;left:10px;top:9px;font-size:6px;letter-spacing:1.2px;color:#fff;line-height:1.4}
  .sachet__flavor{position:absolute;left:10px;top:34px;font-size:10px;font-weight:600;letter-spacing:2px;color:var(--gold)}
  .sachet .leaf-art{right:0;top:0;width:130px;height:58px}

  /* back */
  .back__art{position:absolute;left:0;top:0;width:120px;height:70px;background:linear-gradient(135deg,rgba(0,0,0,.06),rgba(0,0,0,0))}
  .back .brand{right:14px;top:18px}
  .back .brand__dot{width:10px;height:10px;margin-bottom:4px}
  .back .brand__name{font-size:17px}
  .back__intro{position:absolute;left:12px;right:12px;top:70px;font-size:5.6px;line-height:1.55;letter-spacing:.2px}
  .nutrition{position:absolute;left:8px;top:132px;width:76px;border:1px solid var(--tone);padding:3px 4px;font-size:4.2px;line-height:1.5;color:var(--ink)}
  .nutrition__title{font-size:5px;font-weight:600;color:var(--tone);letter-spacing:.6px;border-bottom:1.5px solid var(--tone);padding-bottom:1px}
  .nutrition__row{display:flex;justify-content:space-between;border-bottom:.5px solid var(--tone)}
  .nutrition__row--strong{font-weight:600;color:var(--tone)}
  .nutrition__row--sub{padding-left:5px}
  .nutrition__row:last-child{border-bottom:0}
  .ingredients{position:absolute;left:90px;top:132px;width:134px;height:206px;background:var(--tone);padding:6px 8px;color:#fff}
  .ingredients__row{font-size:5.2px;line-height:1.5;padding:6px 0 7px;border-bottom:1px solid var(--rule-light);min-height:30px}
  .ingredients__code{font-weight:600;font-size:7px;margin-right:3px}
  .ingredients__company{position:absolute;right:8px;bottom:8px;text-align:right;font-size:4.6px;line-height:1.5}

  /* side panel: how it works */
  .side{position:absolute;left:774px;top:720px;width:70px;height:348px;background:var(--paper);box-shadow:0 8px 18px rgba(0,0,0,.08);--tone:var(--hibiscus)}
  .side__band{position:absolute;left:0;top:126px;width:70px;height:222px;background:var(--tone)}
  .step{position:absolute;left:10px;width:50px;text-align:center;font-size:4.6px;line-height:1.4;letter-spacing:.4px}
  .step__art{width:26px;height:22px;margin:0 auto 3px;border-radius:3px;background:rgba(0,0,0,.07)}
  .side__band .step{color:#fff}
  .side__band .step__art{background:rgba(255,255,255,.2)}
</style>
</head>
<body>
<main class="canvas">

  <!-- Fronts -->
  <section class="pack front pack--hibiscus" style="left:278px;top:80px">
    <div class="brand"><span class="brand__dot"></span><span class="brand__name">BrimLeaf</span></div>
    <div class="front__band">
      <div class="front__flavor">HIBISCUS RED TEA</div>
      <div class="front__list">
        <div class="front__item front__item--lead">PREMIUM<br>INSTANT TEA</div>
        <div class="front__item front__item--small">COLD BREWED<br>INSTANT TEA</div>
        <div class="front__item front__item--small">COLD OR HOT<br>WATER DISSOLVER</div>
      </div>
      <div class="front__count">10 SACHETS</div>
      <div class="leaf-art" role="img" aria-label="Line drawing of a tea branch with leaves"></div>
    </div>
  </section>

  <section class="pack front pack--lemon" style="left:536px;top:80px">
    <div class="brand"><span class="brand__dot"></span><span class="brand__name">BrimLeaf</span></div>
    <div class="front__band">
      <div class="front__flavor">LEMON BLACK TEA</div>
      <div class="front__list">
        <div class="front__item front__item--lead">PREMIUM<br>INSTANT TEA</div>
        <div class="front__item front__item--small">COLD BREWED<br>INSTANT TEA</div>
        <div class="front__item front__item--small">COLD OR HOT<br>WATER DISSOLVER</div>
      </div>
      <div class="front__count">10 SACHETS</div>
      <div class="leaf-art" role="img" aria-label="Line drawing of a tea branch with leaves"></div>
    </div>
  </section>

  <!-- Sachets -->
  <div class="sachet sachet--hibiscus" style="left:520px;top:470px">
    <div class="sachet__cap"><div class="brand"><span class="brand__dot"></span><span class="brand__name">BrimLeaf</span></div></div>
    <div class="sachet__body">
      <div class="sachet__sub">PREMIUM<br>INSTANT TEA</div>
      <div class="sachet__flavor">HIBISCUS</div>
      <div class="leaf-art" role="img" aria-label="Line drawing of tea leaves"></div>
    </div>
  </div>
  <div class="sachet sachet--lemon" style="left:470px;top:548px">
    <div class="sachet__cap"><div class="brand"><span class="brand__dot"></span><span class="brand__name">BrimLeaf</span></div></div>
    <div class="sachet__body">
      <div class="sachet__sub">PREMIUM<br>INSTANT TEA</div>
      <div class="sachet__flavor">LEMON BLACK TEA</div>
      <div class="leaf-art" role="img" aria-label="Line drawing of tea leaves"></div>
    </div>
  </div>

  <div class="section-divider"></div>

  <!-- Backs -->
  <section class="pack back pack--lemon" style="left:278px;top:720px">
    <div class="back__art" role="img" aria-label="Faint line drawing of a tea branch"></div>
    <div class="brand"><span class="brand__dot"></span><span class="brand__name">BrimLeaf</span></div>
    <p class="back__intro">Experience the new generation of tea! BrimLeaf® is one of the world fist premium instant tea. Made from real fruit and whole tea leaf, you get incredible tea in seconds. Based on patented cold-brewed technology provide you with the essence of tea, without the need for sugar or preservatives. Brim with health, Brim with taste!</p>
    <div class="nutrition">
      <div class="nutrition__title">NUTRITION FACTS</div>
      <div>10 servings per container<br>Serving size 1 sachet (0.6g)</div>
      <div class="nutrition__row">Amount per serving</div>
      <div class="nutrition__row nutrition__row--strong"><span>Calories</span><span>0</span></div>
      <div class="nutrition__row" style="justify-content:flex-end">% Daily Value*</div>
      <div class="nutrition__row nutrition__row--strong"><span>Total Fat 0g</span><span>0%</span></div>
      <div class="nutrition__row nutrition__row--sub"><span>Saturated Fat 0g</span><span>0%</span></div>
      <div class="nutrition__row nutrition__row--sub"><span>Trans Fat 0g</span><span></span></div>
      <div class="nutrition__row nutrition__row--strong"><span>Cholesterol 0mg</span><span>0%</span></div>
      <div class="nutrition__row nutrition__row--strong"><span>Sodium 0g</span><span>0%</span></div>
      <div class="nutrition__row nutrition__row--strong"><span>Total Carbohydrate 0g</span><span>0%</span></div>
      <div class="nutrition__row nutrition__row--sub"><span>Dietary Fiber 0g</span><span>0%</span></div>
      <div class="nutrition__row nutrition__row--sub"><span>Total Sugars 0g</span><span></span></div>
      <div class="nutrition__row nutrition__row--strong"><span>Protein 0mg</span><span></span></div>
      <div class="nutrition__row"><span>Vitamin D 0mg</span><span>0%</span></div>
      <div class="nutrition__row"><span>Calcium 0mg</span><span>0%</span></div>
      <div class="nutrition__row"><span>Iron 0mg</span><span>0%</span></div>
      <div class="nutrition__row"><span>Potassium 0mg</span><span>0%</span></div>
    </div>
    <div class="ingredients">
      <div class="ingredients__row"><span class="ingredients__code">GB</span>Ingredients: Lemon, black tea</div>
      <div class="ingredients__row"><span class="ingredients__code">N</span>Ingredienser: Sitron, svart te</div>
      <div class="ingredients__row"><span class="ingredients__code">SE</span>Ingredienser: Citron, svart te</div>
      <div class="ingredients__row"><span class="ingredients__code">DK</span>Ingredienser: Citron, sort te</div>
      <div class="ingredients__row" style="border-bottom:0"><span class="ingredients__code">FN</span>Ainesosat: Sitruuna, musta tee</div>
      <div class="ingredients__company">Distributed by Korvenet AS®<br>PO BOX: 4027<br>Oslo, Mørkedalsgata 5, Norway<br>Learn more at BrimLeaf.example</div>
    </div>
  </section>

  <section class="pack back pack--hibiscus" style="left:536px;top:720px">
    <div class="back__art" role="img" aria-label="Faint line drawing of a tea branch"></div>
    <div class="brand"><span class="brand__dot"></span><span class="brand__name">BrimLeaf</span></div>
    <p class="back__intro">Experience the new generation of tea! BrimLeaf® is one of the world fist premium instant tea. Made from real fruit and whole tea leaf, you get incredible tea in seconds. Based on patented cold-brewed technology provide you with the essence of tea, without the need for sugar or preservatives. Brim with health, Brim with taste!</p>
    <div class="nutrition">
      <div class="nutrition__title">NUTRITION FACTS</div>
      <div>10 servings per container<br>Serving size 1 sachet (0.6g)</div>
      <div class="nutrition__row">Amount per serving</div>
      <div class="nutrition__row nutrition__row--strong"><span>Calories</span><span>0</span></div>
      <div class="nutrition__row" style="justify-content:flex-end">% Daily Value*</div>
      <div class="nutrition__row nutrition__row--strong"><span>Total Fat 0g</span><span>0%</span></div>
      <div class="nutrition__row nutrition__row--sub"><span>Saturated Fat 0g</span><span>0%</span></div>
      <div class="nutrition__row nutrition__row--sub"><span>Trans Fat 0g</span><span></span></div>
      <div class="nutrition__row nutrition__row--strong"><span>Cholesterol 0mg</span><span>0%</span></div>
      <div class="nutrition__row nutrition__row--strong"><span>Sodium 0g</span><span>0%</span></div>
      <div class="nutrition__row nutrition__row--strong"><span>Total Carbohydrate 0g</span><span>0%</span></div>
      <div class="nutrition__row nutrition__row--sub"><span>Dietary Fiber 0g</span><span>0%</span></div>
      <div class="nutrition__row nutrition__row--sub"><span>Total Sugars 0g</span><span></span></div>
      <div class="nutrition__row nutrition__row--strong"><span>Protein 0mg</span><span></span></div>
      <div class="nutrition__row"><span>Vitamin D 0mg</span><span>0%</span></div>
      <div class="nutrition__row"><span>Calcium 0mg</span><span>0%</span></div>
      <div class="nutrition__row"><span>Iron 0mg</span><span>0%</span></div>
      <div class="nutrition__row"><span>Potassium 0mg</span><span>0%</span></div>
    </div>
    <div class="ingredients">
      <div class="ingredients__row"><span class="ingredients__code">GB</span>Ingredients: Hibiscus, rose, black tea and stevia extract</div>
      <div class="ingredients__row"><span class="ingredients__code">N</span>Ingredienser: Hibiscus, rose, svart te og stevia ekstrakt</div>
      <div class="ingredients__row"><span class="ingredients__code">SE</span>Ingredienser: Hibiskus, ros, svart te och steviaextrakt</div>
      <div class="ingredients__row"><span class="ingredients__code">DK</span>Ingredienser: Hibiscus, rose, sort te og steviaekstrakt</div>
      <div class="ingredients__row" style="border-bottom:0"><span class="ingredients__code">FN</span>Ainesosat: Hibiskus, ruusu, musta tee, steviauute</div>
      <div class="ingredients__company">Distributed by Korvenet AS®<br>PO BOX: 4027<br>Oslo, Mørkedalsgata 5, Norway<br>Learn more at BrimLeaf.example</div>
    </div>
  </section>

  <!-- Side panel: preparation steps -->
  <aside class="side" aria-label="How it works">
    <div class="step" style="top:14px"><div class="step__art" role="img" aria-label="Sketch of an opened sachet"></div>Open sachet</div>
    <div class="step" style="top:66px"><div class="step__art" role="img" aria-label="Sketch of crystals pouring into a glass"></div>Pour crystals</div>
    <div class="side__band">
      <div class="step" style="top:24px"><div class="step__art" role="img" aria-label="Sketch of water being added"></div>Add 200–300 ml water</div>
      <div class="step" style="top:92px"><div class="step__art" role="img" aria-label="Sketch of a drink being stirred"></div>Stir or shake, enjoy</div>
    </div>
  </aside>

</main>
</body>
</html>
```